Lamp Across Borders- a non profit locin TZ , east Africa. Needing to attract donors.

A flyer for donors /potential partners. showing what their giving has accomplished this year. An Encouraging way to say thank you at the same time informing the partner of the amazing things God is doing with their generous, faithful giving. We will need to print/email. Thank you for considering this project. Your efforts help in educating and feeding 225 street children, providing a safe haven and trade school for hundreds of women and abused teenagers, medical ship on the longest lake in the world going into unreached people groups, a Bible College Training up pastors to plant churches all over TZ, Congo, Burundi and beyond, youth and children’s kids clubs and youth camps. These are the main areas of lamp across borders. Bible college, primary school, trade schools, youth camps/kids clubs. We need help in making sure readers will be drawn to seeing/reading more which leads to donations without overwhelming with too much info. HELP! I can tell you about Jesus I have even authored 7 books, but making s flyer that makes sense it out of my wheelhouse. Again, thank you.
Updates

I do not want longer I need quicker and paid for a 3 day quote. All pictures and logo are on our website. I have tried to send pictures but they won’t send. Please look at. Www.lampacrossborderstz-example.org

Target Market(s)

Professional adults, large companies, donors

Industry/Entity Type

Non profit missionary Lamp Across Borders in Tanzania, Congo, USA and soon to be Canada.

Requirements
Must have
• Color professional pictures, feel good, exciting want to be apart of what God is doing
Nice to have
• Glossy trifold
Should not have
• Fly in the face, guilt feeling, animals in Africa

```html
<!DOCTYPE html>
<html lang="en">
<head>
<meta charset="utf-8">
<title>Lamp Across Borders – Trifold Brochure</title>
<link rel="stylesheet" href="https://fonts.googleapis.com/css2?family=Poppins:wght@300;400;500;600;700;800&family=Oswald:wght@300;400;500&display=swap">
<style>
:root{
  --green:#3cb96a;
  --green-dark:#2e9c57;
  --lime:#cfdc98;
  --ink:#2b2b2b;
  --body:#3a3a3a;
  --band:#313134;
  --paper:#ffffff;
  --canvas:#ececec;
  --grey-line:#b9b9b9;
}
*{box-sizing:border-box;margin:0;padding:0}
html,body{width:1200px;height:2289px;overflow:hidden}
body{background:var(--canvas);font-family:"Poppins",sans-serif;color:var(--body);position:relative}
.spread{position:absolute;left:0;width:1200px;height:849px;background:var(--paper);overflow:hidden;box-shadow:0 10px 30px rgba(0,0,0,.18)}
.spread--outside{top:240px}
.spread--inside{top:1199px}
.panel{position:absolute;top:0;width:400px;height:849px}
.p1{left:0}.p2{left:400px}.p3{left:800px}
.abs{position:absolute}
.copy{font-size:9.2px;line-height:1.32;text-align:justify;color:var(--body)}
.copy p{margin-bottom:8px}
.h-section{font-weight:800;font-size:27px;color:var(--ink);letter-spacing:-.2px;line-height:1}
.h-section span{color:var(--green)}
.h-sub{font-weight:700;font-size:17px;color:var(--ink);line-height:1}
.accent{color:var(--green);font-weight:600}
.rail{position:absolute;left:30px;width:1px;background:var(--grey-line)}
.rail::before{content:"";position:absolute;left:-4px;top:-9px;width:9px;height:9px;border-radius:50%;background:var(--grey-line)}
.photo{position:absolute}
/* outside */
.about-title{left:45px;top:50px}
.about-copy{left:45px;top:88px;width:310px}
.building{left:0;top:610px;width:400px;height:239px;background:linear-gradient(180deg,#d8dde2 0%,#aab1b6 45%,#7d8772 100%);clip-path:polygon(0 18%,100% 0,100% 100%,0 100%)}
.icon-badge{position:absolute;width:48px;height:48px;border-radius:50%;background:#fff;border:1.5px solid #ddd;display:flex;align-items:center;justify-content:center}
.partner-title{left:45px;top:112px;font-size:25px}
.partner-copy{left:45px;top:143px;width:310px;font-size:8.6px;line-height:1.3}
.help-title{left:45px;top:222px;font-size:25px;line-height:1.02}
.help-copy{left:45px;top:283px;width:310px}
.donate-pill{left:45px;top:382px;height:23px;padding:0 14px;border-radius:12px;background:var(--lime);color:#1f6b3a;font-size:10.5px;font-weight:700;display:flex;align-items:center}
.teacher-box{left:0;top:435px;width:260px;height:214px;background:var(--lime)}
.teacher-notch{left:0;top:409px}
.teacher-title{left:45px;top:452px;font-size:26px;font-weight:800;line-height:1.02;color:var(--ink)}
.teacher-title span{color:var(--green)}
.teacher-copy{left:45px;top:555px;width:150px;font-size:8.6px;line-height:1.3;text-align:justify}
.info-band{left:0;top:649px;width:800px;height:200px;background:var(--band)}
.contact{color:#fff;font-size:15px;font-weight:300;line-height:1.3}
.addr{left:87px;top:694px}
.web{left:87px;top:764px}
.contact-icon{position:absolute;left:45px}
.band-rule{position:absolute;left:45px;top:826px;width:200px;height:1px;background:var(--green)}
.dot-btn{position:absolute;top:812px;width:28px;height:28px;border-radius:50%;background:var(--green)}
.cover{left:0;top:0;width:400px;height:649px;background:var(--green)}
.cover-line1{left:0;width:400px;top:34px;text-align:center;font-weight:300;font-size:60px;color:#fff;line-height:1}
.cover-line2{left:0;width:400px;top:90px;text-align:center;font-weight:800;font-size:102px;color:#1d1d1d;line-height:1;letter-spacing:-2px}
.cover-line3{left:0;width:400px;top:184px;text-align:center;font-size:32px;color:#1d1d1d;line-height:1;font-weight:300}
.cover-line3 b{font-weight:700}
.cover-tag{left:0;width:400px;top:255px;text-align:center;font-size:15.5px;line-height:1.25;color:#1d1d1d}
.cover-tag b{color:#fff;font-weight:700}
.people{left:-140px;top:330px;width:540px;height:319px;
  background:
    radial-gradient(ellipse 28% 45% at 18% 70%,#b0705a 0%,rgba(176,112,90,0) 100%),
    radial-gradient(ellipse 30% 45% at 58% 55%,#d9b59c 0%,rgba(217,181,156,0) 100%),
    radial-gradient(ellipse 30% 50% at 85% 75%,#3f62b0 0%,rgba(63,98,176,0) 100%),
    linear-gradient(180deg,#8fcf9f 0%,#6f8a6a 100%);
  -webkit-mask-image:linear-gradient(180deg,transparent 0%,#000 28%);
  mask-image:linear-gradient(180deg,transparent 0%,#000 28%)}
.brand{left:0;width:400px;top:668px;text-align:center;font-family:"Oswald",sans-serif;font-weight:500;color:var(--lime);font-size:52px;line-height:1}
.verse{left:0;width:400px;top:806px;text-align:center;font-family:"Oswald",sans-serif;font-weight:300;color:#fff;font-size:13.5px}
.country{left:0;width:400px;top:826px;text-align:center;font-weight:700;color:#fff;font-size:13px;letter-spacing:.5px}
/* inside */
.serve-bg{left:0;top:0;width:400px;height:849px;background:var(--green)}
.serve-title{left:45px;top:52px;color:#fff;font-size:27px}
.serve-title span{color:#fff}
.sub-row{position:absolute;left:45px;display:flex;align-items:center;gap:8px}
.edu-row{top:98px}
.kids-row{top:358px}
.edu-copy{left:45px;top:130px;width:310px}
.kids-copy{left:45px;top:389px;width:310px}
.car-photo{left:0;top:575px;width:400px;height:274px;background:linear-gradient(180deg,#cfe3c3 0%,#b59c7a 50%,#8a7660 100%);clip-path:polygon(0 8%,45% 0,100% 20%,100% 100%,0 100%)}
.classroom{left:0;top:0;width:400px;height:364px;background:linear-gradient(180deg,#c9b58c 0%,#8c7a62 45%,#a84040 78%,#4a4040 100%)}
.village-row{top:410px}
.village-copy{left:45px;top:447px;width:310px}
.micro-row{top:634px}
.micro-copy{left:45px;top:673px;width:310px}
.testi-head{left:0;top:0;width:400px;height:106px;background:var(--lime)}
.testi-notch{left:315px;top:105px}
.testi-title{left:0;width:400px;top:48px;text-align:center;font-size:26px;font-weight:700;color:var(--ink)}
.card{position:absolute;left:45px;width:310px;border:1.5px dashed #8a8a8a;border-radius:6px}
.card1{top:190px;height:328px}
.card2{top:548px;height:277px}
.avatar{position:absolute;left:70px;width:84px;height:84px;border-radius:50%;background:radial-gradient(circle at 50% 40%,#8a6a55 0%,#4a6b4a 70%,#2f5a3a 100%);border:3px solid #fff}
.av1{top:152px}.av2{top:509px}
.person{position:absolute;left:70px;font-size:19px;font-weight:700;color:var(--green)}
.n1{top:236px}.n2{top:616px}
.c1{left:70px;top:262px;width:270px;font-size:8.8px}
.c2{left:70px;top:642px;width:270px;font-size:8.8px}
</style>
</head>
<body>

<section class="spread spread--outside">
  <div class="panel p1">
    <div class="rail" style="top:48px;height:540px"></div>
    <h2 class="abs h-section about-title">ABOUT <span>US</span></h2>
    <div class="abs copy about-copy">
      <p>Lamp Across Borders (LAB) has its headquarters in Kigoma, Tanzania, on the longest lake in the world – Lake Tanganyika. It is also the second deepest lake in the world, at close to a mile deep. Over 2 million people live around its shores. Four different countries – Congo, Zambia, Burundi, and Tanzania – have their borders in the lake. Kigoma is a strategic port city. Goods are sent by train from Tanzania's eastern seaport, on the Indian Ocean, to Kigoma's port and loaded on ships to reach the land-locked countries surrounding the lake.</p>
      <p>Daniel and Ruth Okoye founded Lamp Across Borders in 2007, but the non-profit has grown much more substantial than just the two of them. Today LAB has six nationals on the missionary staff and employs 45 other locals who help carry on the ministry. Our objective is to raise up nationals who see Jesus as the primary need in this and every nation. Our goal is to make disciples – that's what Jesus told us to do in Matthew 28:19-20. Ultimately that is the only hope any nation has. Our mission is: "To bring hope to the nations through the knowledge of Jesus Christ and the Word of God." (Matt. 12:21)</p>
      <p>How do you bring hope to a nation? There are so many things that can and need to be done in Kigoma, one of the poorest regions in Tanzania. However, we believe it starts with education – and not just a secular education, though that is necessary. The only way to bring hope and affect change in the whole nation is to teach people about Jesus. We approach that goal in many different ways. One is to raise up a new generation that will become godly influencers. There is also a need to educate pastors. Those who are responsible for equipping the Church for the work of the ministry. Starting at each end of the spectrum became our heart's desire.</p>
      <p>Through our Primary School, children are growing up with an excellent education and a strong relationship with Jesus. They are already becoming godly influencers in their families and communities – and soon, the nation! Through our Bible College, pastors are trained on how to study and teach the Word of God. Many of our grads have gone on to plant churches and start other ministries that serve their communities.</p>
      <p>Through LAB, the hope that is found in Jesus Christ is starting to infiltrate this nation and its neighbors.</p>
    </div>
    <div class="photo building" role="img" aria-label="Photo of the two-storey school and college building in Kigoma"></div>
  </div>

  <div class="panel p2">
    <div class="rail" style="top:48px;height:330px"></div>
    <div class="icon-badge" style="left:45px;top:52px">
      <svg width="28" height="26" viewBox="0 0 28 26"><path d="M14 25 C4 17 1 12 1 7.5 A6.5 6.5 0 0 1 14 5 A6.5 6.5 0 0 1 27 7.5 C27 12 24 17 14 25Z" fill="#e53935"/></svg>
    </div>
    <h2 class="abs h-section partner-title">PARTNER <span>WITH US</span></h2>
    <p class="abs copy partner-copy">By partnering with Lamp Across Borders, you are never simply a "sponsor" or "donor"; you are changing lives in East Africa.</p>
    <div class="icon-badge" style="left:45px;top:170px">
      <svg width="30" height="28" viewBox="0 0 30 28"><path d="M15 13 C9 8.5 8 6 8 4.5 A3.3 3.3 0 0 1 15 3.5 A3.3 3.3 0 0 1 22 4.5 C22 6 21 8.5 15 13Z" fill="#e53935"/><path d="M2 20 L9 16 L17 18 Q19 19 17 20.5 L11 20 M9 24 L17 24 L27 17 Q28 15 26 15.5 L19 19" fill="none" stroke="#3b7bd4" stroke-width="1.6" stroke-linecap="round"/></svg>
    </div>
    <h2 class="abs h-section help-title">HOW YOUR<br><span>DONATION HELPS</span></h2>
    <p class="abs copy help-copy">By partnering with Lamp Across Borders, you are never simply a <span class="accent">"sponsor" or "donor"</span>. You are assisting in making disciples and making Jesus known in Tanzania. You will enable children to receive an education, provide scholarships for pastors to be properly trained, and help struggling families learn vocations to support themselves. You can also visit us here, in Kigoma, Tanzania and serve alongside us!</p>
    <div class="abs donate-pill">lampacrossborderstz-example.org/donate</div>

    <svg class="abs teacher-notch" width="40" height="27" viewBox="0 0 40 27"><polygon points="0,0 40,27 0,27" fill="#cfdc98"/></svg>
    <div class="abs teacher-box"></div>
    <h3 class="abs teacher-title">ARE YOU A<br>BIBLE<br><span>TEACHER?</span></h3>
    <p class="abs copy teacher-copy">We depend on visiting pastors / Bible teachers. Come make an impact on students who hunger to learn God's word.</p>

    <div class="abs info-band"></div>
    <svg class="contact-icon" style="top:694px" width="26" height="30" viewBox="0 0 26 30"><path d="M13 29 C5 19 2 14 2 10 A11 11 0 0 1 24 10 C24 14 21 19 13 29Z" fill="#cfdc98"/><circle cx="13" cy="10" r="4.5" fill="#313134"/></svg>
    <p class="abs contact addr">PO Box 4410<br>Millbrook, CA 95199</p>
    <svg class="contact-icon" style="top:764px" width="24" height="24" viewBox="0 0 24 24"><g fill="none" stroke="#cfdc98" stroke-width="2"><circle cx="12" cy="12" r="10"/><ellipse cx="12" cy="12" rx="4.5" ry="10"/><line x1="2" y1="12" x2="22" y2="12"/><line x1="4" y1="6.5" x2="20" y2="6.5"/><line x1="4" y1="17.5" x2="20" y2="17.5"/></g></svg>
    <p class="abs contact web">lampacrossborderstz-example.org</p>
    <div class="band-rule"></div>
    <div class="dot-btn" style="left:254px"></div>
    <div class="dot-btn" style="left:290px"></div>
  </div>

  <div class="panel p3">
    <div class="abs cover"></div>
    <h1 class="abs cover-line1">TO BRING</h1>
    <div class="abs cover-line2">HOPE</div>
    <div class="abs cover-line3">TO THE <b>NATIONS</b></div>
    <p class="abs cover-tag">through the knowledge of Jesus<br>Christ and the <b>Word of God.</b></p>
    <div class="photo people" role="img" aria-label="Photo of three smiling women standing arm in arm"></div>
    <div class="abs brand">LAMP ACROSS<br>BORDERS</div>
    <p class="abs verse">"In His name the nations will put their hope."&nbsp;&nbsp;Mt.12:21</p>
    <p class="abs country">TANZANIA</p>
  </div>
</section>

<section class="spread spread--inside">
  <div class="panel p1">
    <div class="abs serve-bg"></div>
    <div class="rail" style="top:56px;height:20px;background:#fff"></div>
    <h2 class="abs h-section serve-title">HOW WE SERVE</h2>
    <div class="sub-row edu-row">
      <svg width="34" height="26" viewBox="0 0 34 26"><g fill="none" stroke="#fff" stroke-width="1.8" stroke-linejoin="round"><polygon points="17,2 32,9 17,16 2,9"/><path d="M8 12 V19 Q17 25 26 19 V12"/><line x1="32" y1="9" x2="32" y2="17"/></g></svg>
      <span class="h-sub">EDUCATION</span>
    </div>
    <div class="abs copy edu-copy">
      <p>Our vision is to raise up a generation of godly influencers. These are young people who are firmly grounded in their relationship with Jesus Christ. They have received the best education, enabling them to take up positions of influence in every area of their nation. We started with a preschool, which over the years grew into a primary school with over 200 students.</p>
      <p>At the other end of the spectrum, we felt a call to equip the current leaders of the local churches by forming a Bible College.</p>
      <p>Only around 5% of pastors in our region had received any Bible training whatsoever.</p>
      <p>Today pastors are being trained in the Word of God – how to study and how to teach. Many of our grads have gone on to plant churches and start other ministries that serve their communities.</p>
    </div>
    <div class="sub-row kids-row">
      <svg width="34" height="28" viewBox="0 0 34 28"><g fill="none" stroke="#fff" stroke-width="1.8" stroke-linejoin="round"><polygon points="4,12 17,3 30,12"/><rect x="6" y="12" width="22" height="14"/><rect x="14" y="17" width="6" height="9"/><line x1="17" y1="3" x2="17" y2="0"/></g></svg>
      <span class="h-sub">KID'S CLUBS</span>
    </div>
    <div class="abs copy kids-copy">
      <p>Kid's Clubs started as an outreach to children who survive on the streets. During the 2 hour weekly gatherings, the children receive food, play games, and learn everything from the most basic hygiene practices to the most-essential Word of God.</p>
      <p>This ministry has grown from 19 kids and 5 leaders in the first week, to over 1000 kids and more than 70 leaders in 14 different locations from Kigoma to almost 100 miles south on Lake Tanganyika.</p>
      <p>We hold annual summer camps for youth to refresh and recruit new leaders to the program. We also hold Kid's camps to teach and encourage those children who have been a part of Kid's Clubs during the year.</p>
    </div>
    <div class="photo car-photo" role="img" aria-label="Photo of a ministry team sitting on top of a four-wheel-drive vehicle"></div>
  </div>

  <div class="panel p2">
    <div class="photo classroom" role="img" aria-label="Photo of a teacher reading a picture book to children seated on a classroom floor"></div>
    <div class="rail" style="top:400px;height:20px"></div>
    <div class="sub-row village-row">
      <svg width="32" height="28" viewBox="0 0 32 28"><g fill="none" stroke="#3cb96a" stroke-width="1.8" stroke-linejoin="round"><polygon points="2,14 10,7 18,14"/><rect x="4" y="14" width="12" height="12"/><polygon points="14,9 23,2 31,9"/><rect x="17" y="9" width="12" height="17"/><rect x="21" y="18" width="4" height="8"/></g></svg>
      <span class="h-sub">VILLAGE OUTREACHES</span>
    </div>
    <div class="abs copy village-copy">
      <p>Our village outreaches are an exciting time to bring help and hope to remote villages along Lake Tanganyika. We have seen much fruit from these outreaches over the years.</p>
      <p>The outreach can consist of many different parts, such as seeking out candidates for the Bible College. Setting up new Kid's Clubs, a variety of medical training and services, seminars, Jesus film at night, and door-to-door evangelism are also a part of our outreach.</p>
      <p>We happily host teams from North America who feel the call to join us in outreach.</p>
    </div>
    <div class="sub-row micro-row">
      <svg width="32" height="30" viewBox="0 0 32 30"><g fill="none" stroke="#3cb96a" stroke-width="1.8" stroke-linejoin="round"><circle cx="11" cy="7" r="5"/><path d="M2 28 V21 Q2 15 11 15 Q20 15 20 21 V28"/><rect x="19" y="17" width="11" height="11"/><line x1="22" y1="17" x2="22" y2="14"/><line x1="27" y1="17" x2="27" y2="14"/></g></svg>
      <span class="h-sub">MICRO-BUSINESSES</span>
    </div>
    <div class="abs copy micro-copy">
      <p>Jobs are hard to come by. However, through our Vocational Training Center, men and women are given the skills needed to help them support their families.</p>
      <p>Training has included sewing, jewelry making, bread baking, welding, concrete finishing, and business skills. If you have a trade to teach, we would love to host you.</p>
      <p>We have also been able to grant Micro-Business Loans to get our grads started in their own business.</p>
    </div>
  </div>

  <div class="panel p3">
    <div class="abs testi-head"></div>
    <svg class="abs testi-notch" width="40" height="30" viewBox="0 0 40 30"><polygon points="0,0 40,0 40,30" fill="#cfdc98"/></svg>
    <h2 class="abs testi-title">TESTIMONIALS</h2>

    <div class="card card1"></div>
    <div class="avatar av1" role="img" aria-label="Portrait photo of Baraka"></div>
    <h3 class="person n1">BARAKA</h3>
    <div class="abs copy c1">
      <p>Baraka graduated in 2008. He and his family serve in Uvira, Congo, D.R.C. He has planted a growing church in a village that the rebels attack regularly. When that happens, Baraka and his family hide out in their home, praying for the insurgents to leave.</p>
      <p>Baraka wrote us a message: "We are waiting for the gunshots to stop so we may go outside and see what is left. Then bring the Good News to desperate people."</p>
      <p>He has also started a small Bible College where he teaches classes he learned at Lamp Across Borders Bible College.</p>
      <p>Pray for continued safety for his family and church. We are praying about starting a branch of Lamp Across Borders in Congo (DRC).</p>
    </div>

    <div class="card card2"></div>
    <div class="avatar av2" role="img" aria-label="Portrait photo of Neema and Rehema"></div>
    <h3 class="person n2">NEEMA AND REHEMA</h3>
    <div class="abs copy c2">
      <p>Neema and Rehema graduated from Lamp Across Borders Bible College in 2011. They are both sought after speakers throughout East Africa.</p>
      <p>When Neema and Rehema started at LABC, they did not know who they were in Christ. Their confidence was low. Neema never finished high school, yet she knew God wanted her to attend Bible College. Rehema hungered to know more about God's word. They both speak at women's conferences all over East Africa, bringing the truth and power to women.</p>
      <p>Pray for these mighty women of God and the women's ministries they have started.</p>
    </div>
  </div>
</section>

</body>
</html>
```